Football blog needs a Wordpress design new site

We need a wordpress design for a new football blog site. We would like to see a design that uses the colours green, white and black and one that makes good use of the slideshow widgets as scene in the site 'www.trenvix.net'
We would like a modern and sleek looking site but one that is also professional and easy to navigate.
Unfortunately due to unforeseen circumstances we are having to shorten the deadline date for this project.
The new deadline date is 16/07/2014.
We apologise for any inconveniance
It Professional

```html
<!DOCTYPE html>
<html lang="en">
<head>
<meta charset="utf-8">
<title>Match Ledger – Blog</title>
<link href="https://fonts.googleapis.com/css2?family=Lato:wght@300;400;700&family=Open+Sans+Condensed:wght@700&display=swap" rel="stylesheet">
<style>
:root{
  --green:#2ea043;
  --green-dark:#258a37;
  --ink:#222;
  --text:#555;
  --muted:#9a9a9a;
  --rule:#e3e3e3;
  --white:#fff;
  --band:#2b3034;
  --footer:#303538;
  --footer-deep:#24282a;
  --chip:#3b4145;
  --chip-text:#9aa0a4;
}
*{box-sizing:border-box;margin:0;padding:0}
html,body{width:1200px;height:2625px;overflow:hidden}
body{position:relative;background:var(--white);font-family:"Lato",sans-serif;color:var(--text)}
.abs{position:absolute}

/* top strip */
.topbar{left:0;top:0;width:1200px;height:28px;border-bottom:1px solid var(--rule)}
.topbar .dot{position:absolute;top:4px;width:20px;height:20px;border-radius:50%}

/* header */
.header{left:0;top:28px;width:1200px;height:88px;border-bottom:1px solid var(--rule)}
.brand{position:absolute;left:116px;top:26px;display:flex;align-items:center;gap:10px}
.brand .mark{width:36px;height:36px;border-radius:50%;background:var(--green)}
.brand .name{font-size:26px;font-weight:700;color:var(--green-dark)}
.nav{position:absolute;top:34px;left:0;font-size:14.5px;color:#333}
.nav span{position:absolute;white-space:nowrap}
.nav .active{color:var(--green)}
.caret{display:inline-block;width:6px;height:6px;border-right:1.5px solid #777;border-bottom:1.5px solid #777;transform:rotate(45deg);margin-left:6px;vertical-align:3px}

/* slider */
.tile{position:absolute;overflow:hidden}
.tile .caption{position:absolute;left:16px;bottom:14px;color:var(--white);font-family:"Open Sans Condensed",sans-serif;font-size:17px;white-space:nowrap}
.tile.big .caption{font-size:26px;left:26px;bottom:28px}
.tag{display:inline-block;background:var(--green);color:var(--white);font-family:"Lato",sans-serif;font-size:10px;padding:3px 8px;margin:0 4px 6px 0;text-transform:uppercase}
.tile.big .tag{font-size:12px}

/* latest posts */
.section-title{left:140px;top:494px;width:915px;display:flex;align-items:center;gap:16px;font-size:27px;font-weight:300;color:var(--green)}
.section-title::after{content:"";flex:1;height:2px;background:var(--green)}
.card{position:absolute;top:545px;width:208px}
.card .thumb{height:130px;position:relative}
.date{position:absolute;left:12px;top:12px;width:38px;height:38px;border-radius:50%;background:var(--green);color:var(--white);text-align:center;font-size:15px;font-weight:700;line-height:1;padding-top:7px}
.date small{display:block;font-size:9px;font-weight:400;margin-top:1px}
.card h4{font-size:14px;font-weight:400;color:var(--ink);margin-top:12px}
.by{font-size:11px;color:var(--muted);margin-top:3px}
.card p{font-size:11.5px;line-height:18px;color:var(--muted);margin-top:8px}

/* posts */
.post{position:absolute;left:140px;width:680px}
.post .image{height:233px}
.post h3{font-size:21px;font-weight:400;color:var(--ink);margin-top:14px}
.post .by{margin-top:5px}
.meta{border-top:1px solid var(--rule);border-bottom:1px solid var(--rule);margin-top:12px;height:30px;display:flex;align-items:center;gap:24px;font-size:11.5px;color:var(--muted)}
.meta i{display:inline-block;width:10px;height:9px;border:1.3px solid var(--muted);border-radius:2px;margin-right:8px;vertical-align:-1px}
.post p{font-size:11.5px;line-height:19px;color:var(--text);margin-top:10px}

/* pagination */
.pager{left:140px;top:2147px;display:flex}
.pager span{width:26px;height:27px;border:1px solid var(--rule);margin-right:-1px;font-size:11px;color:#777;display:flex;align-items:center;justify-content:center}
.pager .current{background:var(--green);border-color:var(--green);color:var(--white)}

/* sidebar */
.side-title{left:847px;top:832px;font-size:16px;font-weight:400;color:var(--ink)}
.tabs-box{left:847px;top:872px;width:210px;height:540px;border:1px solid var(--rule);border-bottom-width:3px}
.tabs{display:flex;height:34px;font-size:11.5px}
.tabs span{flex:1;display:flex;align-items:center;justify-content:center}
.tabs .on{color:var(--green);border-top:2px solid var(--green)}
.tabs .off{background:#eee;color:var(--muted)}
.pop{position:absolute;left:15px;width:180px}
.pop .img{height:112px}
.pop h5{font-size:13px;font-weight:400;color:var(--ink);margin-top:10px}
.pop .by{font-size:10.5px;margin-top:3px}
.pop p{font-size:11px;line-height:19px;color:var(--muted);margin-top:6px}
.ad{left:851px;top:1442px;width:209px;height:172px;background:linear-gradient(135deg,#3b2a58,#1d1830 60%,#8a2640);padding:24px 12px;color:#ff4a5f;font-size:18px;font-weight:700}
.ad .btn{position:absolute;right:12px;bottom:12px;background:var(--white);color:#222;font-size:8px;padding:3px 6px}

/* newsletter */
.newsletter{left:0;top:2206px;width:1200px;height:81px;background:var(--band)}
.newsletter .lead{position:absolute;left:142px;top:31px;font-size:15px;color:var(--white)}
.newsletter .field{position:absolute;left:644px;top:24px;width:286px;height:36px;background:var(--white);font-size:11px;color:#999;padding:11px 14px}
.newsletter .submit{position:absolute;left:942px;top:24px;width:111px;height:36px;background:var(--green);color:var(--white);font-size:12px;display:flex;align-items:center;justify-content:center}

/* footer */
.footer{left:0;top:2287px;width:1200px;height:281px;background:var(--footer);color:var(--white)}
.f-name{position:absolute;left:142px;top:122px;width:220px;text-align:center;font-size:24px;font-weight:700;color:var(--white)}
.f-head{position:absolute;top:50px;font-size:13px;font-weight:700}
.tweet{position:absolute;left:398px;top:90px;width:205px;font-size:11px;line-height:17px;color:#c9cdd0}
.tweet .who{display:flex;align-items:center;gap:10px;color:var(--white);font-size:12px;margin-bottom:10px}
.tweet .who i{width:26px;height:26px;background:#2aa3ef}
.tweet a{color:#3fb0f2;text-decoration:none}
.tweet .ago{color:var(--white);margin-top:4px;font-size:10.5px}
.tweet .all{border-top:1px solid #444a4e;margin-top:10px;padding-top:14px;color:#3fb0f2}
.chips{position:absolute;left:614px;top:92px;width:210px;display:flex;flex-wrap:wrap;gap:4px}
.chips span{background:var(--chip);color:var(--chip-text);font-size:10.5px;padding:7px 12px}
.follow{position:absolute;left:851px;top:92px;width:210px;display:grid;grid-template-columns:repeat(5,32px);gap:10px}
.follow span{width:32px;height:32px;background:var(--chip);display:flex;align-items:center;justify-content:center}
.follow span i{width:12px;height:12px;border-radius:50%;background:#b7bcc0}
.follow span.on{background:var(--green)}
.follow span.on i{background:var(--white)}
.copy{left:0;top:2568px;width:1200px;height:57px;background:var(--footer-deep);font-size:11px;color:#8a9094}
.copy span{position:absolute;top:22px}
</style>
</head>
<body>

<div class="abs topbar">
  <span class="dot" style="left:886px;background:#3b5a9a"></span>
  <span class="dot" style="left:912px;background:#2aa3ef"></span>
  <span class="dot" style="left:948px;background:#1a77b0"></span>
  <span class="dot" style="left:983px;background:#f38a1c"></span>
  <span class="dot" style="left:1013px;background:#dd4b39"></span>
  <span class="dot" style="left:1045px;background:#c8232c"></span>
</div>

<header class="abs header">
  <div class="brand"><span class="mark"></span><span class="name">Match Ledger</span></div>
  <nav class="nav">
    <span style="left:486px">Home</span>
    <span style="left:570px">World Cup</span>
    <span style="left:674px">Teams<i class="caret"></i></span>
    <span style="left:762px">Standings<i class="caret"></i></span>
    <span class="active" style="left:868px">Blog<i class="caret"></i></span>
    <span style="left:942px">Subscribe</span>
    <span style="left:1038px;top:0">
      <svg width="20" height="20" viewBox="0 0 20 20"><circle cx="8" cy="8" r="6" fill="none" stroke="#888" stroke-width="1.6"/><line x1="12.5" y1="12.5" x2="18" y2="18" stroke="#888" stroke-width="1.8"/></svg>
    </span>
  </nav>
</header>

<section class="slider">
  <div class="tile" style="left:0;top:132px;width:100px;height:160px;background:linear-gradient(160deg,#c9a58c,#6d5a52)" role="img" aria-label="Photo of a shouting goalkeeper">
    <div class="caption" style="left:-70px">Corrupti quos dolores etquas</div></div>
  <div class="tile" style="left:0;top:308px;width:100px;height:162px;background:linear-gradient(160deg,#e0713a,#8f3e22)" role="img" aria-label="Photo of a player in an orange shirt">
    <div class="caption" style="left:-70px">Corrupti quos dolores etquas</div></div>
  <div class="tile" style="left:116px;top:132px;width:230px;height:338px;background:linear-gradient(170deg,#4d7f3c,#e2c83a 45%,#2f6b30)" role="img" aria-label="Photo of players in yellow shirts celebrating">
    <div class="caption"><span class="tag">Sample Tag</span><br>Corrupti quos dolores etquas</div></div>
  <div class="tile big" style="left:363px;top:132px;width:458px;height:338px;background:linear-gradient(160deg,#6b8a5a,#d9d9d6 40%,#7d8b6c 75%,#3e5a34)" role="img" aria-label="Photo of two players in white shirts celebrating a goal">
    <div class="caption"><span class="tag">Germany</span><span class="tag">World Cup</span><br>Corrupti quos dolores etquas</div></div>
  <div class="tile" style="left:837px;top:132px;width:229px;height:160px;background:linear-gradient(160deg,#d9c43c,#3d8a3a)" role="img" aria-label="Photo of fans in yellow and green in the stands">
    <div class="caption"><span class="tag">Sample Tag</span><br>Corrupti quos dolores etquas</div></div>
  <div class="tile" style="left:837px;top:308px;width:229px;height:162px;background:linear-gradient(160deg,#e8c44a,#a88740 55%,#4d7a3a)" role="img" aria-label="Photo of a smiling fan in sunglasses">
    <div class="caption"><span class="tag">Sample Tag</span><br>Corrupti quos dolores etquas</div></div>
  <div class="tile" style="left:1080px;top:132px;width:120px;height:338px;background:linear-gradient(170deg,#c78f77,#b9332c 60%,#7a1f1c)" role="img" aria-label="Photo of a player in a red shirt shouting">
    <div class="caption"><span class="tag">Sample Tag</span><br>Corrupti quos dolores</div></div>
</section>

<h2 class="abs section-title">Latest Posts</h2>

<article class="card" style="left:142px">
  <div class="thumb" style="background:linear-gradient(160deg,#6d8f4a,#c9c5b8 55%,#4f7a3a)" role="img" aria-label="Photo of a ball on the pitch line"><div class="date">15<small>nov</small></div></div>
  <h4>Your Title Post Here</h4><div class="by">by John Doe</div>
  <p>Quisque placerat nec mauris ut moles- tie. Pellentesque venenatis quam ut justo tincidunt.</p>
</article>
<article class="card" style="left:377px">
  <div class="thumb" style="background:linear-gradient(160deg,#3d5a9a,#d77a2e 55%,#4f8a3a)" role="img" aria-label="Photo of players contesting the ball"><div class="date">16<small>nov</small></div></div>
  <h4>Your Title Post Here</h4><div class="by">by John Doe</div>
  <p>Quisque placerat nec mauris ut moles- tie. Pellentesque venenatis quam ut justo tincidunt.</p>
</article>
<article class="card" style="left:614px">
  <div class="thumb" style="background:linear-gradient(160deg,#8a2a2a,#c9302c 50%,#3a2a2a)" role="img" aria-label="Photo of a team in red celebrating"><div class="date">16<small>nov</small></div></div>
  <h4>Your Title Post Here</h4><div class="by">by John Doe</div>
  <p>Quisque placerat nec mauris ut moles- tie. Pellentesque venenatis quam ut justo tincidunt.</p>
</article>
<article class="card" style="left:849px">
  <div class="thumb" style="background:linear-gradient(160deg,#3b8a3a,#e8c84a 50%,#d9a88a)" role="img" aria-label="Photo of a fan holding a flag"><div class="date">15<small>nov</small></div></div>
  <h4>Your Title Post Here</h4><div class="by">by John Doe</div>
  <p>Quisque placerat nec mauris ut moles- tie. Pellentesque venenatis quam ut justo tincidunt.</p>
</article>

<article class="post" style="top:833px">
  <div class="image" style="background:linear-gradient(160deg,#5a8a3a,#7aa44a 50%,#3f7030)" role="img" aria-label="Photo of a match in play near the goal"></div>
  <h3>Blog Image and Text Post</h3>
  <div class="by">by John Doe &nbsp;|&nbsp; 15 November, 2013</div>
  <div class="meta"><span><i></i>34 comments</span><span><i></i>Graphic Design, Web Design, Awesome, Social</span></div>
  <p>Cras tristique sem eu justo ornare venenatis. Nam condimentum nec sapien ut porttitor. Etiam purus mauris, pretium et lorem eget, sagittis sollicitudin ligula. Morbi dolor nulla, lacinia posuere fringilla ut, lobortis ut turpis.</p>
</article>
<article class="post" style="top:1256px">
  <div class="image" style="background:linear-gradient(160deg,#3f8a3a,#e6d43a 40%,#c98a6a 70%,#a83a2a)" role="img" aria-label="Photo of fans in green wigs and novelty glasses"></div>
  <h3>Blog Image and Text Post</h3>
  <div class="by">by John Doe &nbsp;|&nbsp; 15 November, 2013</div>
  <div class="meta"><span><i></i>34 comments</span><span><i></i>Graphic Design, Web Design, Awesome, Social</span></div>
  <p>Cras tristique sem eu justo ornare venenatis. Nam condimentum nec sapien ut porttitor. Etiam purus mauris, pretium et lorem eget, sagittis sollicitudin ligula. Morbi dolor nulla, lacinia posuere fringilla ut, lobortis ut turpis.</p>
</article>
<article class="post" style="top:1680px">
  <div class="image" style="background:linear-gradient(160deg,#7a8a5a,#c9b89a 45%,#a0322a 70%,#3a7ab8)" role="img" aria-label="Photo of a referee showing a card to a player"></div>
  <h3>Blog Image and Text Post</h3>
  <div class="by">by John Doe &nbsp;|&nbsp; 15 November, 2013</div>
  <div class="meta"><span><i></i>34 comments</span><span><i></i>Graphic Design, Web Design, Awesome, Social</span></div>
  <p>Cras tristique sem eu justo ornare venenatis. Nam condimentum nec sapien ut porttitor. Etiam purus mauris, pretium et lorem eget, sagittis sollicitudin ligula. Morbi dolor nulla, lacinia posuere fringilla ut, lobortis ut turpis.</p>
</article>

<div class="abs pager">
  <span>&#8249;</span><span>1</span><span class="current">2</span><span>3</span><span>4</span><span>5</span><span>6</span><span>&#8250;</span>
</div>

<aside>
  <h3 class="abs side-title">Read the Top Stories!</h3>
  <div class="abs tabs-box">
    <div class="tabs"><span class="on">Popular Post</span><span class="off">Recent Post</span></div>
    <div class="pop" style="top:52px">
      <div class="img" style="background:linear-gradient(170deg,#3a6a9a,#e6c83a 55%,#2f6aa8)" role="img" aria-label="Photo of a team lined up for a group picture"></div>
      <h5>Your Post Title Demo</h5><div class="by">November 15, 2013</div>
      <p>Pellentesque habitant morbi tristique senectus et netus et malesuada fames...</p>
    </div>
    <div class="pop" style="top:289px">
      <div class="img" style="background:linear-gradient(160deg,#e6c84a,#3f8a3a 60%,#2a5a9a)" role="img" aria-label="Photo of a fan with a flag"></div>
      <h5>Your Post Title Demo</h5><div class="by">November 15, 2013</div>
      <p>Pellentesque habitant morbi tristique senectus et netus et malesuada fames...</p>
    </div>
  </div>
  <div class="abs ad" role="img" aria-label="Advert for football boots">Strikeline<br>boots<span class="btn">SHOP NOW</span></div>
</aside>

<section class="abs newsletter">
  <p class="lead">Subscribe to our newsletter and get the latest football updates!</p>
  <div class="field">Email</div>
  <div class="submit">Submit</div>
</section>

<footer class="abs footer">
  <div class="f-name">Match Ledger</div>

  <h4 class="f-head" style="left:398px">Latest Tweet</h4>
  <div class="tweet">
    <div class="who"><i></i>Match Ledger</div>
    Lorem ipsum dolor sit amet, consectetur adipiscing elit. Curabitur ut blandit sapien. <a>http://mledger.net/p7wq2</a>
    <div class="ago">2 days ago</div>
    <div class="all">See all tweets</div>
  </div>

  <h4 class="f-head" style="left:614px">Tags</h4>
  <div class="chips">
    <span>Awesome</span><span>Football</span><span>Worldcup</span><span>Germany</span><span>WFA</span><span>Marlowe</span><span>ECFU</span><span>WFA Standings</span><span>Ravinho</span><span>ACFU</span>
  </div>

  <h4 class="f-head" style="left:851px">Follow us!</h4>
  <div class="follow">
    <span><i></i></span><span class="on"><i></i></span><span><i></i></span><span><i></i></span><span><i></i></span>
    <span><i></i></span><span><i></i></span><span><i></i></span><span><i></i></span><span><i></i></span>
  </div>
</footer>

<div class="abs copy">
  <span style="left:142px">Copyright © 2014 - Match Ledger</span>
  <span style="left:815px">Privacy Policy</span>
  <span style="left:933px">Terms and Conditions</span>
</div>

</body>
</html>
```